Upmarket designer fashion & gift boutique card design

I need a business card that captures the vision of my customer & store. I am a ladies fashion boutique in the beautiful Northern Beaches of Sydney. I stock top australian designer fashion that is bold, colourful, & eccentric. My store also carries quirky & retro gift ware & unique statement jewellery. I want a card that is as colourful & eccentric as the designers I stock & the customer I attract. I love bold bright colours, leopard print, abstract or geometric shapes but nothing to fluffy or girly. I have attached my logo which is to be included on one side of the card.

Target Market(s)

25+ with a strong focus on the fabulous 30's & 40's

Industry/Entity Type

Boutique

Contact Information for Business Card

Delia Marchant, Director, Shop 5/17 Kellering Crescent Tarrowin Bay NSW 2186, delia@tullaverra.com.au ABN 71 308 916 254, mobile number 0438 762 104 www.facebook.com/tullaverra

Font styles to use
Sans Serif

Colors

Designer to choose colors to be used in the design.

Requirements
Must have
• Open mind- although leopard or zebra print would win some votes
Nice to have
• Unique, fun,bold, quirky & different - hit me with your best shot!
Should not have
• No swirly/running writing text please

```html
<!DOCTYPE html>
<html lang="en">
<head>
<meta charset="UTF-8">
<title>Tullaverra – Business Card</title>
<link rel="stylesheet" href="https://fonts.googleapis.com/css2?family=Josefin+Sans:wght@300;400;600&display=swap">
<style>
  :root {
    --page: #ffffff;
    --gold-dark: #a8711f;
    --gold-mid: #d7a24a;
    --gold-light: #f3d58e;
    --champagne: #efe6d2;
    --cream: #f9f6ee;
    --paper-shadow: #cbbfa6;
    --ink: #2a2620;
    --logo-ink: #2c8fa8;
  }
  * { margin: 0; padding: 0; box-sizing: border-box; }
  html, body {
    width: 886px; height: 1200px; overflow: hidden;
    background: var(--page);
    font-family: "Josefin Sans", sans-serif;
  }
  .sheet { position: relative; width: 886px; height: 1200px; }

  .card {
    position: absolute; left: 0; width: 886px;
    border: 14px solid var(--gold-mid);
    border-image: linear-gradient(135deg, var(--gold-dark), var(--gold-light) 40%, var(--gold-mid) 60%, var(--gold-dark)) 1;
    overflow: hidden;
  }
  .card--front { top: 0; height: 574px; }
  .card--back { top: 621px; height: 579px; }

  .card__damask {
    position: absolute; inset: 0;
    background:
      radial-gradient(ellipse at 50% 50%, rgba(255,250,235,0.75), rgba(255,250,235,0) 60%),
      linear-gradient(90deg, var(--gold-dark) 0%, var(--gold-mid) 14%, var(--champagne) 40%, var(--champagne) 60%, var(--gold-mid) 86%, var(--gold-dark) 100%);
  }

  .card__band {
    position: absolute; left: -14px; width: 886px; height: 256px;
  }
  .card--front .card__band { top: 198px; }
  .card--back .card__band { top: 168px; }
  .card__band svg { display: block; width: 100%; height: 100%; }
  .band-shadow { fill: var(--paper-shadow); }
  .band-paper { fill: var(--cream); }

  .brand {
    position: absolute; left: 184px; top: 292px;
    font-weight: 600; font-size: 78px; letter-spacing: -1px;
    color: var(--logo-ink); line-height: 1;
  }
  .brand__tagline {
    position: absolute; left: 470px; top: 396px;
    font-weight: 300; font-size: 22px; color: var(--ink);
  }

  .contact {
    position: absolute; left: -14px; width: 886px; top: 196px;
    text-align: center; color: var(--ink);
    font-weight: 300; font-size: 23px; line-height: 29.5px; letter-spacing: 1.5px;
  }
</style>
</head>
<body>
<div class="sheet">

  <section class="card card--front">
    <div class="card__damask" role="img" aria-label="Gold and cream damask pattern background"></div>
    <div class="card__band">
      <svg viewBox="0 0 886 256" preserveAspectRatio="none" aria-hidden="true">
        <polygon class="band-shadow" points="0,14 40,8 80,16 120,10 170,18 210,9 260,15 300,7 350,16 400,11 450,17 500,8 550,14 600,10 650,18 700,9 750,15 800,7 850,13 886,10 886,250 840,256 790,248 740,256 690,251 640,256 590,247 540,255 490,249 440,256 390,250 340,256 290,247 240,254 190,249 140,256 90,248 40,255 0,250"/>
        <polygon class="band-paper" points="0,10 40,4 80,12 120,6 170,14 210,5 260,11 300,3 350,12 400,7 450,13 500,4 550,10 600,6 650,14 700,5 750,11 800,3 850,9 886,6 886,246 840,252 790,244 740,254 690,247 640,253 590,243 540,251 490,245 440,254 390,246 340,252 290,243 240,250 190,245 140,253 90,244 40,251 0,246"/>
      </svg>
    </div>
    <div class="brand">tullaverra</div>
    <div class="brand__tagline">Gift and Fashion</div>
  </section>

  <section class="card card--back">
    <div class="card__damask" role="img" aria-label="Gold and cream damask pattern background"></div>
    <div class="card__band">
      <svg viewBox="0 0 886 256" preserveAspectRatio="none" aria-hidden="true">
        <polygon class="band-shadow" points="0,14 40,8 80,16 120,10 170,18 210,9 260,15 300,7 350,16 400,11 450,17 500,8 550,14 600,10 650,18 700,9 750,15 800,7 850,13 886,10 886,250 840,256 790,248 740,256 690,251 640,256 590,247 540,255 490,249 440,256 390,250 340,256 290,247 240,254 190,249 140,256 90,248 40,255 0,250"/>
        <polygon class="band-paper" points="0,10 40,4 80,12 120,6 170,14 210,5 260,11 300,3 350,12 400,7 450,13 500,4 550,10 600,6 650,14 700,5 750,11 800,3 850,9 886,6 886,246 840,252 790,244 740,254 690,247 640,253 590,243 540,251 490,245 440,254 390,246 340,252 290,243 240,250 190,245 140,253 90,244 40,251 0,246"/>
      </svg>
    </div>
    <address class="contact" style="font-style: normal;">
      Delia Marchant, Director,<br>
      Shop 5/17 Kellering Crescent<br>
      Tarrowin Bay NSW 2186,<br>
      delia@tullaverra.com.au<br>
      ABN 71 308 916 254,<br>
      mobile number 0438 762 104<br>
      www.facebook.com/tullaverra
    </address>
  </section>

</div>
</body>
</html>
```